New telco company needs a product page

We need to design two pages - one index and one inner.

We are a new telco company and we have developed our own phone. We will be selling our services and the phone on this site.

The design should be easy to understand and use, following the latest trends in Web design, be clean. It should communicate professionalism and integrity.

The name of our company is VORO which stands for Value Over Rush Often. The design should follow this principle.

Our company logo is attached. I can send it in other colors/sizes - let me know.

Target Market(s)

Aging population (70+), middle-aged with parents and grandparents.

Industry/Entity Type

It Company

Requirements
Must have
• index page, inner page, flat, clean, Pellucor 5 style / ZEB style (quintel.example), easy navigation, fluid layout, CSS, tableless
Should not have
• should not use old fonts, should not use old-style design, should not have animation, should not look like QDX or Bimzo (too busy)

```html
<!DOCTYPE html>
<html lang="en">
<head>
<meta charset="utf-8">
<title>VORO — Value Over Rush Often</title>
<link rel="stylesheet" href="https://fonts.googleapis.com/css2?family=Source+Sans+3:wght@300;400;600&display=swap">
<style>
  :root {
    --header-bg: #7b797b;
    --nav-top: #6c6c6e;
    --nav-bottom: #2c2c2e;
    --nav-divider: #1c1c1c;
    --nav-highlight: #7e7e80;
    --white: #ffffff;
    --ink: #333333;
    --ink-soft: #6a6a6a;
    --hero-light: #f3f3f3;
    --hero-mid: #dcdcdc;
    --caption-band: rgba(40, 40, 40, 0.72);
    --footer-bg: #0e0e0e;
    --social-blue: #3b5bb0;
    --social-sky: #2aa9e0;
    --social-orange: #f26a1c;
    --social-red: #e02a26;
    --search-ink: #9a9a9a;
  }
  * { box-sizing: border-box; margin: 0; padding: 0; }
  html, body {
    width: 1200px; height: 1079px; overflow: hidden;
    font-family: "Source Sans 3", "Helvetica Neue", Arial, sans-serif;
    background: var(--white); color: var(--ink);
  }
  .page { position: relative; width: 1200px; height: 1079px; }

  .site-header { position: absolute; top: 0; left: 0; width: 1200px; height: 126px; background: var(--header-bg); }
  .brand { position: absolute; left: 86px; top: 28px; display: flex; align-items: center; gap: 14px; }
  .brand-name { font-size: 62px; font-weight: 300; color: var(--white); letter-spacing: 2px; line-height: 1; }
  .brand-mark { width: 22px; height: 22px; background: var(--white); }
  .search { position: absolute; left: 887px; top: 60px; width: 227px; height: 34px; background: var(--white); border-radius: 3px; border: 1px solid #d8d8d8; display: flex; align-items: center; padding: 0 10px; }
  .search-placeholder { flex: 1; font-size: 13px; font-style: italic; color: var(--search-ink); }

  .main-nav { position: absolute; top: 126px; left: 0; width: 1200px; height: 48px; background: linear-gradient(var(--nav-top), var(--nav-bottom)); border-top: 1px solid #5a5a5a; }
  .main-nav ul { list-style: none; position: absolute; left: 86px; top: 0; height: 48px; display: flex; }
  .main-nav li { height: 48px; display: flex; align-items: center; justify-content: center; color: var(--white); font-size: 18px; font-weight: 400; border-left: 1px solid var(--nav-divider); box-shadow: inset 1px 0 0 var(--nav-highlight); }
  .main-nav li:first-child { border-left: none; box-shadow: none; }

  .hero { position: absolute; top: 174px; left: 0; width: 1200px; height: 407px; background: linear-gradient(180deg, var(--hero-light) 0%, #e9e9e9 55%, var(--hero-mid) 100%); }
  .hero-title { position: absolute; top: 52px; left: 0; width: 1200px; padding-left: 60px; text-align: center; font-size: 36px; font-weight: 300; color: var(--ink); }
  .hero-subtitle { position: absolute; top: 114px; left: 0; width: 1200px; text-align: center; font-size: 36px; font-weight: 300; color: var(--ink-soft); }
  .hero-arrow { position: absolute; top: 206px; }
  .hero-arrow.prev { left: 86px; }
  .hero-arrow.next { left: 1090px; }
  .hero-product { position: absolute; left: 300px; top: 238px; width: 648px; height: 110px; border-radius: 30px 30px 40px 40px; background: linear-gradient(180deg, #3a3a3a 0%, #8c8c8c 45%, #4a4a4a 100%); box-shadow: 0 14px 20px rgba(0,0,0,0.18); }

  .features { position: absolute; top: 629px; left: 86px; width: 1026px; display: flex; gap: 18px; }
  .feature { width: 330px; }
  .feature-media { position: relative; height: 198px; }
  .feature-media.about { background: linear-gradient(135deg, #c9b39a 0%, #8aa7c4 55%, #dfe6ee 100%); }
  .feature-media.services { background: linear-gradient(135deg, #6b6d73 0%, #3f86d6 50%, #b8b8ba 100%); }
  .feature-media.testimonials { background: linear-gradient(135deg, #f1f1f1 0%, #d8d3cf 55%, #5a5450 100%); }
  .feature-caption { position: absolute; left: 0; bottom: 0; width: 100%; height: 47px; background: var(--caption-band); display: flex; align-items: center; justify-content: space-between; padding: 0 20px 0 22px; color: var(--white); font-size: 22px; font-weight: 400; }
  .feature-text { margin-top: 16px; text-align: center; font-size: 18px; line-height: 29px; font-weight: 300; color: var(--ink); padding: 0 10px; }

  .site-footer { position: absolute; top: 974px; left: 0; width: 1200px; height: 105px; background: var(--footer-bg); color: var(--white); }
  .footer-links { position: absolute; left: 86px; top: 25px; font-size: 14px; }
  .copyright { position: absolute; left: 86px; top: 59px; font-size: 13px; }
  .social { position: absolute; left: 931px; top: 34px; display: flex; gap: 13px; }
  .social span { width: 36px; height: 36px; display: block; }
  .social .s1 { background: var(--social-blue); }
  .social .s2 { background: var(--social-sky); }
  .social .s3 { background: var(--social-orange); }
  .social .s4 { background: var(--social-red); }
</style>
</head>
<body>
<div class="page">
  <header class="site-header">
    <div class="brand"><span class="brand-name">VORO</span><span class="brand-mark"></span></div>
    <div class="search">
      <span class="search-placeholder">Search..</span>
      <svg width="14" height="14" viewBox="0 0 14 14"><circle cx="6" cy="6" r="4.2" fill="none" stroke="#9a9a9a" stroke-width="2"/><line x1="9" y1="9" x2="12.5" y2="12.5" stroke="#9a9a9a" stroke-width="2.2" stroke-linecap="round"/></svg>
    </div>
  </header>

  <nav class="main-nav">
    <ul>
      <li style="width:106px">HOME</li>
      <li style="width:146px">ABOUT US</li>
      <li style="width:155px">SOLUTIONS</li>
      <li style="width:163px">OUR PHONE</li>
      <li style="width:183px">TESTIMONIALS</li>
      <li style="width:109px">BLOG</li>
      <li style="width:170px">CONTACT US</li>
    </ul>
  </nav>

  <section class="hero" role="img" aria-label="Soft grey city skyline behind the VORO phone">
    <h1 class="hero-title">Duisautem Veleum Iriuredolor Hendrerit Invulputate Velitesse</h1>
    <p class="hero-subtitle">Quamnunc Putamus Claram</p>
    <svg class="hero-arrow prev" width="22" height="58" viewBox="0 0 22 58"><polyline points="19,2 3,29 19,56" fill="none" stroke="#9a9a9a" stroke-width="2"/></svg>
    <svg class="hero-arrow next" width="22" height="58" viewBox="0 0 22 58"><polyline points="3,2 19,29 3,56" fill="none" stroke="#9a9a9a" stroke-width="2"/></svg>
    <div class="hero-product" role="img" aria-label="VORO smartphone lying on its side"></div>
  </section>

  <section class="features">
    <article class="feature">
      <div class="feature-media about" role="img" aria-label="Support staff working at a computer">
        <div class="feature-caption">ABOUT US
          <svg width="22" height="22" viewBox="0 0 22 22"><circle cx="11" cy="11" r="10" fill="#fff"/><path d="M6 11h8M11 7l4 4-4 4" fill="none" stroke="#333" stroke-width="2.2"/></svg>
        </div>
      </div>
      <p class="feature-text">Many of our community partners are stuc kin a corner of their communities that the perceive to be the whole world.</p>
    </article>
    <article class="feature">
      <div class="feature-media services" role="img" aria-label="Hands holding a tablet showing cloud services">
        <div class="feature-caption">SERVICES
          <svg width="22" height="22" viewBox="0 0 22 22"><circle cx="11" cy="11" r="10" fill="#fff"/><path d="M6 11h8M11 7l4 4-4 4" fill="none" stroke="#333" stroke-width="2.2"/></svg>
        </div>
      </div>
      <p class="feature-text">Many of our community partners are stuc kin a corner of their communities that the perceive to be the whole world.</p>
    </article>
    <article class="feature">
      <div class="feature-media testimonials" role="img" aria-label="Businesswoman working on a laptop in an office">
        <div class="feature-caption">TESTIMONIALS
          <svg width="22" height="22" viewBox="0 0 22 22"><circle cx="11" cy="11" r="10" fill="#fff"/><path d="M6 11h8M11 7l4 4-4 4" fill="none" stroke="#333" stroke-width="2.2"/></svg>
        </div>
      </div>
      <p class="feature-text">Many of our community partners are stuc kin a corner of their communities that the perceive to be the whole world.</p>
    </article>
  </section>

  <footer class="site-footer">
    <p class="footer-links">Home | About TNV | News &amp; Media | Projects | Gallery | Blog | Contact</p>
    <p class="copyright">Copyrights 2013. All Rights Reserved.</p>
    <div class="social"><span class="s1"></span><span class="s2"></span><span class="s3"></span><span class="s4"></span></div>
  </footer>
</div>
</body>
</html>
```